Pellmark Ridgeway LLC stationery, business card and web page design.

i need a full set of stationery designed using the name "Pellmark Ridgeway LLC" with a tag line "construction consulting services". using the uploaded monkey icon as the logo.

i like the colors orange, green and black in general but im not limited to that. the company offers consulting services to various types of construction businesses.

i travel around the country in a 4x4 camper offering consulting services and technical training short term and long to various types of construction companies.

Construction Company

Peter Lund
p.lund@pellmarkridgeway.example
2748 Fenwick Rd
Maple Glen, NY 10943
555 014 3627

list these services on the card.

Business Consulting
Capital Investments
Marketing Implementations
Technical Training

1 page

Designer to choose colors to be used in the design.

• company info and use of the monkey icon i provided.
• a fun but professional design
• the color red

```html
<!DOCTYPE html>
<html lang="en">
<head>
<meta charset="utf-8">
<title>Pellmark Ridgeway LLC — Stationery</title>
<link href="https://fonts.googleapis.com/css2?family=Oswald:wght@500&family=Jost:wght@400;500&family=Lato:wght@400&display=swap" rel="stylesheet">
<style>
:root{
  --orange:#e85f33;
  --orange-deep:#cf4f26;
  --ink:#111111;
  --paper:#ffffff;
  --text:#333333;
  --muted:#666666;
  --backdrop:#ebe7e3;
}
*{margin:0;padding:0;box-sizing:border-box}
html,body{width:1200px;height:835px;overflow:hidden;background:var(--backdrop)}
.sheet{position:absolute;overflow:hidden}
.brand{font-family:'Oswald',sans-serif;font-weight:500;text-transform:uppercase;letter-spacing:.06em;white-space:nowrap}
.contact{font-family:'Jost',sans-serif;font-size:6.6px;color:var(--text);line-height:1.35;white-space:nowrap}
.icon{width:5px;height:5px;display:inline-block;vertical-align:middle}
.mark-dot{display:inline-block;border-radius:50%;background:var(--ink);vertical-align:middle}

/* letterhead */
.letterhead{left:56px;top:63px;width:378px;height:486px;background:var(--paper)}
.letterhead .lockup{position:absolute;left:34px;top:60px;display:flex;align-items:center;gap:5px}
.letterhead .lockup .brand{font-size:8.4px;color:var(--orange)}
.letterhead .lockup .mark-dot{width:9px;height:9px}
.letter-body{position:absolute;left:34px;top:142px;width:322px;font-family:'Lato',sans-serif;color:var(--muted)}
.letter-body .greeting{font-size:8.6px;color:var(--text);margin-bottom:5px}
.letter-body p{font-size:4.5px;line-height:1.6;margin-bottom:6px}
.letter-body p.closing{margin-top:12px;width:304px}
.signoff{position:absolute;left:32px;top:352px;font-family:'Lato',sans-serif;text-align:center;width:56px}
.signoff .regards{font-size:7.4px;color:var(--text)}
.signoff .signer{font-size:4.6px;color:var(--muted);margin-top:1px}
.signoff .rule{height:1px;background:var(--ink);margin-top:5px}
.signature{position:absolute;left:32px;top:385px;width:56px;height:26px;background:linear-gradient(180deg,#f2f2f2,#e6e6e6)}
.letter-address{position:absolute;right:32px;top:414px;text-align:right}
.letter-address .gap{height:6px}

/* folder */
.folder{left:454px;top:63px;width:376px;height:486px;background:var(--orange)}
.folder .emblem{position:absolute;left:0;right:0;top:228px;text-align:center;font-size:17px;color:var(--orange-deep)}

/* business card front */
.card-front{left:857px;top:73px;width:282px;height:162px;background:var(--paper)}
.card-front .lockup{position:absolute;right:13px;top:18px;display:flex;align-items:center;gap:4px}
.card-front .lockup .brand{font-size:7.4px;color:var(--ink)}
.card-front .lockup .mark-dot{width:10px;height:10px}
.card-front .person{position:absolute;left:13px;top:89px}
.card-front .name{font-family:'Jost',sans-serif;font-size:11.4px;color:var(--orange);letter-spacing:.02em}
.card-front .role{font-family:'Jost',sans-serif;font-size:5.8px;color:var(--text);margin:1px 0 3px}
.card-front .postal{margin-top:3px}

/* card backs */
.card-back{left:857px;top:342px;width:282px;height:162px;background:var(--orange)}
.card-dark{left:857px;top:610px;width:282px;height:161px;background:var(--ink)}
.card-back .brand,.card-dark .brand{position:absolute;left:0;right:0;top:70px;text-align:center;font-size:12.6px}
.card-back .brand{color:var(--paper)}
.card-dark .brand{color:var(--orange)}
.card-back .site,.card-dark .site{position:absolute;left:0;right:0;top:143px;text-align:center;font-family:'Jost',sans-serif;font-size:5.4px;color:#f3f3f3}

/* envelope */
.envelope{left:56px;top:574px;width:378px;height:200px;background:var(--orange)}
.envelope .flap{position:absolute;left:0;top:0;width:378px;height:36px;background:var(--orange);border-radius:0 0 14px 14px;box-shadow:0 2px 3px rgba(0,0,0,.22)}
.envelope .flap .brand{position:absolute;left:0;right:0;top:10px;text-align:center;font-size:11px;color:var(--paper)}
.envelope .lockup{position:absolute;right:14px;bottom:20px;display:flex;align-items:center;gap:5px}
.envelope .lockup .brand{font-size:9px;color:var(--ink)}
.envelope .lockup .mark-dot{width:14px;height:14px}

/* compliment slip */
.slip{left:454px;top:574px;width:365px;height:200px;background:var(--paper)}
.slip .title{position:absolute;right:18px;top:16px;font-size:10px;color:var(--orange)}
.slip .lockup{position:absolute;left:17px;top:112px;display:flex;align-items:center;gap:4px}
.slip .lockup .brand{font-size:6.6px;color:var(--ink)}
.slip .lockup .mark-dot{width:11px;height:11px}
.slip .details{position:absolute;left:17px;top:165px}
.slip .postal{position:absolute;right:18px;top:173px;text-align:right}
</style>
</head>
<body>

<svg width="0" height="0" style="position:absolute" aria-hidden="true">
  <defs>
    <symbol id="i-phone" viewBox="0 0 10 10"><path d="M2.2 1h1.6l.8 2.2-1.1.8c.6 1.2 1.4 2 2.5 2.5l.8-1.1L9 6.2v1.6C9 8.5 8.5 9 7.8 9 4.1 8.8 1.2 5.9 1 2.2 1 1.5 1.5 1 2.2 1z" fill="#e85f33"/></symbol>
    <symbol id="i-mail" viewBox="0 0 10 10"><rect x="1" y="2.2" width="8" height="5.6" fill="none" stroke="#e85f33" stroke-width="1.1"/><path d="M1 2.4 5 5.6 9 2.4" fill="none" stroke="#e85f33" stroke-width="1.1"/></symbol>
    <symbol id="i-web" viewBox="0 0 10 10"><circle cx="5" cy="5" r="4" fill="#e85f33"/><path d="M1 5h8M5 1c-1.6 2.4-1.6 5.6 0 8M5 1c1.6 2.4 1.6 5.6 0 8" fill="none" stroke="#fff" stroke-width=".6"/></symbol>
  </defs>
</svg>

<!-- Letterhead -->
<section class="sheet letterhead">
  <div class="lockup"><span class="mark-dot"></span><span class="brand">Pellmark Ridgeway LLC</span></div>
  <div class="letter-body">
    <div class="greeting">Hello Anna,</div>
    <p>Thank you for meeting with us last week about the upcoming project. We have reviewed your site plans, crew schedules and budget notes, and we are ready to outline a consulting plan that fits your timeline. Our team will visit your yard, walk the job with your foremen and prepare a short written report with clear next steps for each phase of the work.</p>
    <p>The proposed program covers business consulting, capital investment planning, marketing implementation and hands-on technical training for your field staff. Training sessions can run for a few days or across several months, depending on what your crews need most. Each session is built around real tasks on your own sites, so new skills are put to use right away. We also review your estimating process, equipment costs and hiring plans, and we suggest simple changes that save time and money. Progress reports are shared every two weeks, and we stay in contact by phone and email between visits so that questions never slow the work down.</p>
    <p>Our consultant travels across the country and can arrive at your location within a short notice period. Before the first visit we will send a simple checklist covering permits, safety records, tools and staffing levels. Once the checklist is returned we will confirm dates, agree on the length of the engagement and set goals that can be measured. Fees are fixed for each phase and are listed in the attached summary. If anything in this letter is unclear, please call or write and we will gladly walk you through each part of the plan in more detail.</p>
    <p class="closing">We look forward to working with you and your crews, and we are confident this plan will bring steady, lasting results to every project you take on this year.</p>
  </div>
  <div class="signoff">
    <div class="regards">Regards,</div>
    <div class="signer">Owen Hale</div>
    <div class="rule"></div>
  </div>
  <div class="signature" role="img" aria-label="Handwritten signature of Owen Hale"></div>
  <address class="letter-address contact" style="font-style:normal">
    <div>Po Box 2748</div>
    <div>Post Office NY, 10943</div>
    <div class="gap"></div>
    <div>555 014 3627 <svg class="icon"><use href="#i-phone"/></svg></div>
    <div>info@pellmarkridgeway.example <svg class="icon"><use href="#i-mail"/></svg></div>
    <div>www.pellmarkridgeway.example <svg class="icon"><use href="#i-web"/></svg></div>
  </address>
</section>

<!-- Presentation folder -->
<section class="sheet folder">
  <div class="emblem brand">Pellmark Ridgeway LLC</div>
</section>

<!-- Business card, front -->
<section class="sheet card-front">
  <div class="lockup"><span class="brand">Pellmark Ridgeway LLC</span><span class="mark-dot"></span></div>
  <div class="person">
    <div class="name">Marta Quill</div>
    <div class="role">Director</div>
    <div class="contact"><svg class="icon"><use href="#i-phone"/></svg> 555 014 3627</div>
    <div class="contact"><svg class="icon"><use href="#i-mail"/></svg> info@pellmarkridgeway.example</div>
    <div class="contact"><svg class="icon"><use href="#i-web"/></svg> www.pellmarkridgeway.example</div>
    <div class="contact postal">Po Box 2748 Post Office NY, 10943</div>
  </div>
</section>

<!-- Business card, back -->
<section class="sheet card-back">
  <div class="brand">Pellmark Ridgeway LLC</div>
  <div class="site">www.pellmarkridgeway.example</div>
</section>

<!-- Envelope -->
<section class="sheet envelope">
  <div class="flap"><div class="brand">Pellmark Ridgeway LLC</div></div>
  <div class="lockup"><span class="mark-dot"></span><span class="brand">Pellmark Ridgeway LLC</span></div>
</section>

<!-- Compliment slip -->
<section class="sheet slip">
  <div class="title brand">Pellmark Ridgeway LLC</div>
  <div class="lockup"><span class="mark-dot"></span><span class="brand">Pellmark Ridgeway LLC</span></div>
  <div class="details">
    <div class="contact"><svg class="icon"><use href="#i-phone"/></svg> 555 014 3627</div>
    <div class="contact"><svg class="icon"><use href="#i-mail"/></svg> info@pellmarkridgeway.example</div>
    <div class="contact"><svg class="icon"><use href="#i-web"/></svg> www.pellmarkridgeway.example</div>
  </div>
  <div class="postal contact">
    <div>Po Box 2748</div>
    <div>Post Office NY, 10943</div>
  </div>
</section>

<!-- Business card, dark variant -->
<section class="sheet card-dark">
  <div class="brand">Pellmark Ridgeway LLC</div>
  <div class="site">www.pellmarkridgeway.example</div>
</section>

</body>
</html>
```